Business Card Design

5* Hotel Property based on an island in Greece

My position is aparta from being a director, i'm on the accounts payable too, not sure how this should be stated, with a comma or "/"?

Sorry about the uploaded logo, it was a mistaken one!

There's also need to be added this  www.corvanteholdings.com on the back side of the card!

Also need to have the logo of the corvante holdings which can be found in a second on the brief! Thank you guys, irini

Industry/Entity Type

Business

Contact Information for Business Card

VERISTOKA PELLA Hotel
Irini Dravetsou
Director, AP Dept.

www.veristoka.gr
Peltira Island 85300
Greece

irinidravetsou@fenmail.com
+306951273064

```html
<!DOCTYPE html>
<html lang="en">
<head>
<meta charset="utf-8">
<title>Veristoka Pella Hotel – Business Card</title>
<link href="https://fonts.googleapis.com/css2?family=Anton&family=Questrial&display=swap" rel="stylesheet">
<style>
  :root {
    --bg: #1a1a1a;
    --paper: #ffffff;
    --band: #1d5fa8;
    --band-dark: #15508f;
    --sky: #3aa6df;
    --pale: #8fd0f5;
    --ink: #3a3a3a;
    --muted: #8a8a8a;
  }
  * { box-sizing: border-box; margin: 0; padding: 0; }
  html, body { width: 1200px; height: 1200px; overflow: hidden; background: var(--bg); }
  body { font-family: "Questrial", sans-serif; position: relative; }

  .card {
    position: absolute; left: 160px; width: 880px; height: 500px;
    background: var(--paper); overflow: hidden;
  }
  .card--back { top: 60px; }
  .card--front { top: 640px; }

  /* back side */
  .member {
    position: absolute; left: 292px; top: 84px;
    display: flex; align-items: center; gap: 6px;
    font-size: 15px; letter-spacing: 0.5px; color: var(--muted);
  }
  .member__bar { width: 30px; height: 9px; background: #9a9a9a; }
  .group-mark {
    position: absolute; left: 292px; top: 108px;
    width: 150px; height: 150px; background: var(--band);
  }
  .group-name {
    position: absolute; left: 292px; top: 268px; width: 300px;
    font-size: 34px; line-height: 1.05; color: var(--band);
  }
  .back-band {
    position: absolute; left: 0; bottom: 0; width: 100%; height: 92px;
    background: var(--band);
    display: flex; align-items: center; justify-content: center;
    color: #fff; font-size: 30px; letter-spacing: 4px;
  }

  /* front side */
  .hotel-mark {
    position: absolute; left: 105px; top: 50px;
    width: 145px; height: 145px; border-radius: 50%; background: var(--sky);
  }
  .hotel-name {
    position: absolute; left: 275px; top: 70px;
    font-size: 46px; letter-spacing: 1px; color: var(--ink); line-height: 1;
  }
  .hotel-sub {
    position: absolute; left: 278px; top: 128px;
    font-size: 24px; letter-spacing: 12px; color: var(--ink);
  }
  .front-band {
    position: absolute; left: 0; top: 255px; width: 100%; height: 245px;
    background: linear-gradient(90deg, var(--band-dark), var(--band));
  }
  .person { position: absolute; left: 36px; top: 58px; }
  .person__name {
    font-family: "Anton", sans-serif; font-size: 46px; color: #fff;
    letter-spacing: 0.5px; line-height: 1.05;
  }
  .person__role {
    font-family: "Anton", sans-serif; font-size: 30px; color: var(--pale);
    letter-spacing: 0.5px; line-height: 1.2;
  }
  .stars { position: absolute; left: 432px; top: 18px; }
  .contacts {
    position: absolute; left: 466px; top: 16px; list-style: none;
    color: #fff; font-size: 22px;
  }
  .contacts li { display: flex; align-items: flex-start; gap: 16px; margin-bottom: 14px; }
  .contacts li.address { margin-bottom: 14px; }
  .contacts svg { flex: 0 0 30px; }
  .contacts span { line-height: 30px; }
  .address span { line-height: 27px; }
</style>
</head>
<body>

<section class="card card--back" aria-label="Card back">
  <div class="member"><span class="member__bar"></span>MEMBER OF THE</div>
  <div class="group-mark"></div>
  <div class="group-name">corvante holdings</div>
  <div class="back-band">www.corvanteholdings.com</div>
</section>

<section class="card card--front" aria-label="Card front">
  <div class="hotel-mark"></div>
  <div class="hotel-name">VERISTOKA PELLA</div>
  <div class="hotel-sub">HOTEL</div>

  <div class="front-band">
    <div class="person">
      <div class="person__name">Irini Dravetsou</div>
      <div class="person__role">Director, AP Dept.</div>
    </div>

    <svg class="stars" width="20" height="210" viewBox="0 0 20 210" aria-hidden="true">
      <g fill="#5bb8ec">
        <circle cx="10" cy="10" r="3"/><circle cx="10" cy="50" r="3"/>
        <circle cx="10" cy="95" r="3"/><circle cx="10" cy="135" r="3"/>
        <circle cx="10" cy="175" r="3"/><circle cx="10" cy="205" r="3"/>
      </g>
    </svg>

    <ul class="contacts">
      <li>
        <svg width="30" height="30" viewBox="0 0 30 30" aria-hidden="true">
          <circle cx="15" cy="15" r="14" fill="#5bb8ec"/>
          <rect x="8" y="9" width="14" height="10" rx="1" fill="none" stroke="#1d5fa8" stroke-width="2"/>
          <rect x="12" y="20" width="6" height="2" fill="#1d5fa8"/>
        </svg>
        <span>www.veristoka.gr</span>
      </li>
      <li>
        <svg width="30" height="30" viewBox="0 0 30 30" aria-hidden="true">
          <circle cx="15" cy="15" r="14" fill="#5bb8ec"/>
          <path d="M10 8 l3 0 l1.5 4 l-2 1.5 a9 9 0 0 0 4 4 l1.5 -2 l4 1.5 l0 3 a2 2 0 0 1 -2 2 a13 13 0 0 1 -12 -12 a2 2 0 0 1 2 -2z" fill="#1d5fa8"/>
        </svg>
        <span>+306951273064</span>
      </li>
      <li class="address">
        <svg width="30" height="30" viewBox="0 0 30 30" aria-hidden="true">
          <circle cx="15" cy="15" r="14" fill="#5bb8ec"/>
          <path d="M15 7 a5.5 5.5 0 0 1 5.5 5.5 c0 4 -5.5 10 -5.5 10 s-5.5 -6 -5.5 -10 A5.5 5.5 0 0 1 15 7z" fill="#1d5fa8"/>
          <circle cx="15" cy="12.5" r="2" fill="#5bb8ec"/>
        </svg>
        <span>Peltira Island<br>85300 Greece</span>
      </li>
      <li>
        <svg width="30" height="30" viewBox="0 0 30 30" aria-hidden="true">
          <circle cx="15" cy="15" r="14" fill="#5bb8ec"/>
          <rect x="8" y="10" width="14" height="10" rx="1" fill="#1d5fa8"/>
          <path d="M8 10 l7 6 l7 -6" fill="none" stroke="#5bb8ec" stroke-width="1.5"/>
        </svg>
        <span>irinidravetsou@fenmail.com</span>
      </li>
    </ul>
  </div>
</section>

</body>
</html>
```